Holiday Rental Company Flyer Design (DL not A5)

Note from PixelFolk Administration: The category sizing selected is A5, however the project requires DL sized artwork. Please refer to the DL template link below while the 'Special Requirements' are updated accordingly.

Project Brief:
We need a double sided DL flyer designed for an up market Holiday Rental Company that portrays a personalised approach to property management. These are to be used for letter box drops to homes we're specifically targeting so the design should be modern, complimentary colour palette, uncluttered & visually appealing.

Please Download the DL Template from Quillmark here: http://www.quillmark.com.au/qm/ns/propath/UploadResources.aspx?selectedTab=0?pfid=BFB&pf_id=BFB&xnav=easypath-upload-image#Templates

Target Market(s)

Wealthy Home Owners

Industry/Entity Type

It Company

Font styles to use
Other font styles liked:
• Avant Garde Extra Light & Demi

Colors
33b8a4

Requirements
Must have
• DL Flyer sizes (210mm width x 99mm width, plus 3mm bleed)
• Front: Logo, Main Image & Grab
• Back: Contact Details & Brief Description of our business
• Images: Ideally the main image should be the house with the pool but alternatively a lifestyle images could also be used.
Nice to have
• A creative designer!
Should not have
• Clutter & busy designs

```html
<!DOCTYPE html>
<html lang="en">
<head>
<meta charset="utf-8">
<title>Bayside Havens – Flyer Front</title>
<link rel="stylesheet" href="https://fonts.googleapis.com/css2?family=Questrial&display=swap">
<style>
  :root {
    --sky-top: #a9b4bd;
    --sky-mid: #d3d8da;
    --sky-low: #e8e6df;
    --sea-far: #b9d3e0;
    --sea-near: #6fb2d6;
    --brand-green: #12987a;
    --brand-green-soft: rgba(18, 152, 122, 0.82);
    --text-light: #ffffff;
    --text-soft: rgba(255, 255, 255, 0.85);
  }
  * { margin: 0; padding: 0; box-sizing: border-box; }
  html, body {
    width: 1200px;
    height: 850px;
    overflow: hidden;
    background: #ffffff;
  }
  .flyer {
    position: relative;
    width: 1200px;
    height: 850px;
    overflow: hidden;
    font-family: "Questrial", "Helvetica Neue", Arial, sans-serif;
    color: var(--text-light);
  }
  .scene-photo {
    position: absolute;
    inset: 0;
    background: linear-gradient(
      to bottom,
      var(--sky-top) 0%,
      var(--sky-mid) 22%,
      var(--sky-low) 43%,
      var(--sea-far) 44%,
      #a3c8dc 60%,
      var(--sea-near) 100%
    );
  }
  .chevron-panel {
    position: absolute;
    inset: 0;
    width: 1200px;
    height: 850px;
  }
  .brand-block {
    position: absolute;
    left: 0;
    top: 0;
    width: 540px;
    text-align: center;
  }
  .tagline {
    position: absolute;
    top: 258px;
    left: 40px;
    width: 480px;
    font-size: 24px;
    line-height: 31px;
    letter-spacing: 0.5px;
    color: var(--text-light);
  }
  .tagline-rule {
    position: absolute;
    top: 320px;
    left: 40px;
    width: 482px;
    height: 1px;
    background: var(--text-soft);
  }
  .brand-name {
    position: absolute;
    top: 340px;
    left: 20px;
    width: 500px;
    font-size: 60px;
    line-height: 64px;
    letter-spacing: 9px;
    text-transform: uppercase;
    color: var(--text-light);
  }
  .brand-dot {
    position: absolute;
    top: 488px;
    left: 247px;
    width: 46px;
    height: 46px;
    border: 2px solid var(--text-soft);
    border-radius: 50%;
  }
  .web-address {
    position: absolute;
    top: 592px;
    left: 40px;
    width: 460px;
    font-size: 21px;
    letter-spacing: 1px;
    color: var(--text-soft);
  }
</style>
</head>
<body>
  <main class="flyer">
    <div class="scene-photo" role="img" aria-label="Photograph of a small blue sailing boat resting on a calm, glassy bay under a soft cloudy sky"></div>

    <svg class="chevron-panel" viewBox="0 0 1200 850" aria-hidden="true">
      <polygon fill="var(--brand-green-soft)"
        points="0,0 358,0 388,95 358,191 0,191"/>
      <polygon fill="var(--brand-green)"
        points="0,191 358,191 695,423 358,656 0,656"/>
      <polygon fill="var(--brand-green-soft)"
        points="0,656 358,656 388,755 358,850 0,850"/>
    </svg>

    <section class="brand-block">
      <p class="tagline">Holiday Rental Management<br>With A Difference.</p>
      <div class="tagline-rule"></div>
      <h1 class="brand-name">Bayside<br>Havens</h1>
      <div class="brand-dot"></div>
      <p class="web-address">baysidehavens.com.au</p>
    </section>
  </main>
</body>
</html>
```